Business Card Design

Vintage looking Hair Salon, where the customer service is 100%. We are based in a cottage. With shabby chic console tables and beautiful ornate mirrors..and rich brown leather cutting chairs. Chandeliers at the window, and a ornate patchwork sofa.
our clientele are 28years upwards.. Mums with small children.. Ladies that lunch, and men that want more than a barbers and are prepared to pay for our services.
I am looking for a classy business card.. That look expensive.. Where our initials WHP become a visual reference.. I was thinking of cream card initials in black on a embossed tarnished silver.. But I'm open to suggestion. I want,  need the design to be able to work with flyers price list ect.

Willowmere Hair Parlour
27 Fenwick Row
Ardley Green
bN42 6TW
FB thewillowmerehairparlour
Info@thewillowmerhairparlour.co.uk
0208 715 2964

```html
<!DOCTYPE html>
<html lang="en">
<head>
<meta charset="utf-8">
<title>Willowmere Hair Parlour – Business Card</title>
<link rel="stylesheet" href="https://fonts.googleapis.com/css2?family=Noto+Sans:wght@400;600&display=swap">
<style>
  :root {
    --backdrop: #cbb79c;
    --card-light: #d3eef9;
    --card-mid: #9fd6f1;
    --card-deep: #3ea3dc;
    --pattern: rgba(255, 255, 255, 0.30);
    --pattern-edge: rgba(110, 185, 230, 0.40);
    --frame-line: rgba(255, 255, 255, 0.55);
    --logo-ink: #ffffff;
    --text-ink: #1f3550;
  }
  html, body {
    margin: 0;
    width: 1200px;
    height: 880px;
    overflow: hidden;
    background: var(--backdrop);
  }
  .canvas {
    position: relative;
    width: 1200px;
    height: 880px;
    display: flex;
    align-items: center;
    justify-content: center;
  }
  .business-card {
    position: relative;
    width: 1000px;
    height: 572px;
    overflow: hidden;
    background: linear-gradient(125deg, var(--card-light) 0%, var(--card-mid) 50%, var(--card-deep) 100%);
    box-shadow: 0 6px 18px rgba(60, 40, 20, 0.25);
    font-family: "Noto Sans", Arial, sans-serif;
  }
  .ornament-field {
    position: absolute;
    left: 80px;
    top: 36px;
    width: 840px;
    height: 480px;
    border-radius: 50%;
    background: radial-gradient(ellipse at center, var(--pattern) 0%, rgba(255,255,255,0.14) 60%, rgba(255,255,255,0) 72%);
  }
  .corner-ornament {
    position: absolute;
    width: 170px;
    height: 170px;
    background: radial-gradient(circle at center, var(--pattern-edge) 0%, rgba(255,255,255,0) 70%);
  }
  .corner-ornament.top-left { left: -36px; top: -36px; }
  .corner-ornament.top-right { right: -36px; top: -36px; }
  .corner-ornament.bottom-left { left: -36px; bottom: -36px; }
  .corner-ornament.bottom-right { right: -36px; bottom: -36px; }
  .card-frame {
    position: absolute;
    inset: 0;
    width: 1000px;
    height: 572px;
  }
  .brand-name {
    position: absolute;
    left: 0;
    right: 0;
    top: 70px;
    margin: 0;
    text-align: center;
    color: var(--logo-ink);
    font-weight: 600;
    line-height: 1;
  }
  .brand-name .brand-article {
    display: block;
    font-size: 34px;
    letter-spacing: 2px;
  }
  .brand-name .brand-main {
    display: block;
    margin-top: 4px;
    font-size: 78px;
    letter-spacing: 1px;
  }
  .brand-name .brand-sub {
    display: block;
    margin-top: 6px;
    font-size: 36px;
    letter-spacing: 3px;
  }
  .contact-details {
    position: absolute;
    left: 170px;
    top: 330px;
    margin: 0;
    color: var(--text-ink);
    font-size: 21px;
    line-height: 1.6;
    font-style: normal;
    white-space: nowrap;
  }
  .contact-details .divider { margin: 0 12px; }
</style>
</head>
<body>
<main class="canvas">
  <section class="business-card">
    <div class="ornament-field" role="img" aria-label="Large oval of ornate swirling floral pattern"></div>
    <div class="corner-ornament top-left" role="img" aria-label="Ornate corner flourish"></div>
    <div class="corner-ornament top-right" role="img" aria-label="Ornate corner flourish"></div>
    <div class="corner-ornament bottom-left" role="img" aria-label="Ornate corner flourish"></div>
    <div class="corner-ornament bottom-right" role="img" aria-label="Ornate corner flourish"></div>

    <svg class="card-frame" viewBox="0 0 1000 572" aria-hidden="true">
      <ellipse cx="500" cy="276" rx="410" ry="232" fill="none" stroke="var(--frame-line)" stroke-width="2"/>
      <ellipse cx="500" cy="276" rx="398" ry="222" fill="none" stroke="var(--frame-line)" stroke-width="1"/>
      <rect x="24" y="24" width="952" height="524" rx="10" fill="none" stroke="var(--frame-line)" stroke-width="1.5"/>
    </svg>

    <h1 class="brand-name">
      <span class="brand-article">The</span>
      <span class="brand-main">Willowmere</span>
      <span class="brand-sub">Hair Parlour</span>
    </h1>

    <address class="contact-details">
      <div class="address-line">27 Fenwick Row, Ardley Green, BN42 6TW.</div>
      <div class="online-line">E : info@thewillowmerhairparlour.co.uk<span class="divider">|</span>FB : thewillowmerehairparlour</div>
      <div class="phone-line">PH : 0208 715 2964</div>
    </address>
  </section>
</main>
</body>
</html>
```